Membership Card for our Survival Company

We need a membership card design, front and back for our VIP Membership program. Membership card must be branded with our logo and convey the idea of survivalism.
All members will receive this physical, plastic card with embossed Full Name and unique Membership ID.
ID formatting: "VIP-XXXXXXX"
See example image here:
https://media.pagebrook.net/7k/48b2c91e0a3d5f7e61b8c4d2a9e03f/VIP-Membership-Card1-Reflect.png
Note, this is just an example. We do not require you to follow the size, format, image, etc. The only things that must be included are the:
1) Logo
2) Full Name
3) Membership ID as per the provided format
Any more questions, please let me know.
Industry/Entity Type
It Company
Contact Information for Business Card
Full Name
VIP-XXXXXXX

```html
<!DOCTYPE html>
<html lang="en">
<head>
<meta charset="utf-8">
<title>WildEndure VIP Membership Card</title>
<link href="https://fonts.googleapis.com/css2?family=Pathway+Gothic+One&display=swap" rel="stylesheet">
<style>
  :root {
    --card-white: #ffffff;
    --ink: #1a1a1a;
    --rule: #222222;
    --brand-ink: #5a4a12;
    --band-blue: #1449d8;
  }
  html, body {
    margin: 0;
    padding: 0;
    width: 1200px;
    height: 600px;
    overflow: hidden;
    background: var(--card-white);
  }
  .card {
    position: relative;
    width: 1200px;
    height: 600px;
    background: var(--card-white);
    font-family: "Pathway Gothic One", "Arial Narrow", sans-serif;
    color: var(--ink);
    overflow: hidden;
  }
  .brand-name {
    position: absolute;
    top: 24px;
    right: 52px;
    font-size: 80px;
    line-height: 1;
    color: var(--brand-ink);
    white-space: nowrap;
  }
  .field {
    position: absolute;
    left: 4px;
  }
  .field-label {
    font-size: 66px;
    line-height: 1;
    white-space: nowrap;
  }
  .field-line {
    position: absolute;
    height: 3px;
    background: var(--rule);
  }
  .field-name { top: 138px; }
  .line-name { left: 163px; width: 999px; top: 190px; }
  .field-id { top: 313px; }
  .line-id { left: 372px; width: 790px; top: 363px; }
  .id-prefix {
    position: absolute;
    left: 384px;
    top: 308px;
    font-size: 50px;
    line-height: 1;
  }
  .band {
    position: absolute;
    left: 0;
    bottom: 0;
    width: 100%;
    height: 136px;
    background: linear-gradient(to bottom,
      rgba(20, 73, 216, 0) 0px,
      var(--band-blue) 26px,
      var(--band-blue) 100%);
  }
</style>
</head>
<body>
  <main class="card">
    <span class="brand-name">WildEndure</span>

    <div class="field field-name">
      <span class="field-label">NAME :</span>
    </div>
    <div class="field-line line-name"></div>

    <div class="field field-id">
      <span class="field-label">MEMBERSHIP ID :</span>
    </div>
    <span class="id-prefix">VIP -</span>
    <div class="field-line line-id"></div>

    <div class="band"></div>
  </main>
</body>
</html>
```